Pet sitting Business needs a website

We need a website that shows our services and prices. Shows our love of animals but also our professionalism. want a gallery, about, blog, services, links to fb and instagram accounts, newsletter archive. want it to be easy to access and wonderful to navigate. want the domain to be Birchvalecritterden.com
take any info from FB site www.facebook.com/birchvalecritterden
I would like it to fit tidy frame platform

Target Market(s)

upscale area, responsible pet owners,

Industry/Entity Type

Pet Care

Coding

Coded - Design and coding required

Number of Pages Required

5+ page

Font styles to use
Sans Serif

Requirements
Must have
• (tidy frame platform)
• Menu
• photo gallery
• about us
• services
• policies
• monthly newsletter
• unavailable dates
• Introduction (welcome)
• payment methods
• Daily updates
• testimonials (use from fb site)
Should not have
• stock photos

```html
<!DOCTYPE html>
<html lang="en">
<head>
<meta charset="utf-8">
<title>Birchvale Critter Den — Professional Pet Sitting</title>
<link href="https://fonts.googleapis.com/css2?family=Open+Sans:wght@400;600;700&family=Great+Vibes&display=swap" rel="stylesheet">
<style>
:root{
  --orange:#d88a0b;
  --orange-dark:#b97308;
  --blue:#1a6a9a;
  --blue-dark:#0f5a86;
  --nav-blue:#1c7cb2;
  --ink:#333333;
  --muted:#555555;
  --white:#ffffff;
  --grey:#e6e6e6;
  --sky:#c9dbe6;
  --sand:#d8c3a2;
}
*{margin:0;padding:0;box-sizing:border-box}
html,body{width:1200px;height:3888px;overflow:hidden}
body{position:relative;font-family:"Open Sans",Arial,sans-serif;color:var(--ink);background:var(--white)}
.abs{position:absolute}
.script{font-family:"Great Vibes",cursive;font-weight:400}

/* hero */
.hero{left:0;top:0;width:1200px;height:700px;background:linear-gradient(180deg,var(--sky) 0%,#a9c3d3 55%,var(--sand) 80%,#c9ab80 100%)}
.hero-photo{left:0;top:0;width:1200px;height:700px}
.topbar-email{left:195px;top:88px;font-size:14px;color:var(--blue);display:flex;align-items:center;gap:8px}
.topbar-phone{right:190px;top:88px;font-size:14px;color:var(--blue);display:flex;align-items:center;gap:8px}
.brand{left:470px;top:30px;width:260px;text-align:center;display:flex;align-items:center;justify-content:center;gap:8px}
.brand-dot{width:14px;height:14px;border-radius:50%;background:var(--orange)}
.brand-name{font-size:22px;font-weight:700;color:var(--orange)}
.nav{left:192px;top:132px;width:816px;height:56px;background:linear-gradient(180deg,var(--nav-blue),var(--blue-dark));border-radius:4px;display:flex;align-items:center;box-shadow:0 3px 6px rgba(0,0,0,.25)}
.nav a{color:var(--white);text-decoration:none;font-size:11.5px;font-weight:600;padding:0 13px;height:56px;display:flex;align-items:center;white-space:nowrap}
.nav a.active{background:var(--orange);border-radius:4px 0 0 4px}
.hero-caption{left:362px;top:470px;height:52px;padding:0 26px;background:rgba(15,90,134,.85);color:var(--white);font-size:29px;display:flex;align-items:center}
.hero-arrows{left:574px;top:612px;display:flex;gap:16px}

/* section titles */
.sec-title{width:1200px;left:0;text-align:center;font-size:42px}

/* gallery */
.gallery{left:0;top:700px;width:1200px;height:595px;background:var(--orange)}
.frame{position:absolute;border:6px solid var(--white);box-shadow:0 3px 8px rgba(0,0,0,.3)}
.frame .ph{width:100%;height:100%}
.frame .cap{position:absolute;left:0;bottom:0;width:100%;height:38px;background:rgba(0,0,0,.45);color:var(--white);font-size:14px;display:flex;align-items:center;padding-left:18px}
.frame .cap.blue{background:rgba(15,90,134,.9)}

/* about */
.about{left:0;top:1295px;width:1200px;height:500px;background:linear-gradient(120deg,#d9d9d9,#bdbdbd 50%,#e2e2e2)}
.about-rule{left:335px;top:1440px;width:530px;height:1px;background:#9a9a9a}
.about-portrait{left:220px;top:1475px;width:255px;height:255px;border-radius:50%;border:8px solid var(--orange);background:radial-gradient(circle at 45% 40%,#e2c9a4,#8a6a4a 80%)}
.about-text{left:492px;top:1512px;width:510px;font-size:12px;line-height:2;color:#222}
.about-text p+p{margin-top:18px}

/* services */
.services-band{left:0;top:1795px;width:1200px;height:560px}
.daily-box{left:222px;top:2000px;width:230px;height:252px;background:var(--white);padding:8px;box-shadow:0 3px 8px rgba(0,0,0,.3)}
.daily-box div{width:100%;height:100%;background:var(--orange)}
.daily-title{left:535px;top:1992px;font-size:24px;font-weight:600;color:var(--orange)}
.daily-price{left:535px;top:2022px;font-size:20px;font-weight:700;color:var(--white)}
.daily-price small{font-size:11px;font-weight:400}
.list{list-style:none;font-size:11px;line-height:23px}
.list li{padding-left:22px;position:relative}
.list li::before{content:"";position:absolute;left:4px;top:10px;width:4px;height:4px;border-radius:50%;background:currentColor}
.daily-list{color:var(--white);top:2062px;width:260px}
.btn-details{left:537px;top:2220px;width:112px;height:36px;border-radius:18px;background:var(--orange);color:var(--white);font-size:11px;font-weight:600;display:flex;align-items:center;justify-content:center}

.card-icon{width:112px;height:112px;background:var(--white);padding:5px;box-shadow:0 2px 6px rgba(0,0,0,.3)}
.card-icon div{width:100%;height:100%;background:var(--orange)}
.card-title{font-size:24px;font-weight:600;color:var(--blue)}
.card-price{font-size:22px;font-weight:700;color:var(--blue)}
.card-price small{font-size:14px}
.card-list{color:#333;width:260px}

/* testimonials */
.quote-mark{left:570px;top:3080px;width:60px;height:60px;border-radius:50%;background:var(--orange);color:var(--white);font-size:48px;font-family:Georgia,serif;display:flex;align-items:center;justify-content:center;line-height:1;padding-top:18px}
.quote-text{left:270px;top:3145px;width:660px;text-align:center;color:#d7e6ef;font-size:19px;line-height:1.6}
.avatar{left:543px;top:3265px;width:114px;height:114px;border-radius:50%;border:5px solid var(--white);background:radial-gradient(circle at 50% 45%,#c9a88a,#6e5a4a 85%)}
.t-name{left:0;width:1200px;top:3398px;text-align:center;color:var(--white);font-size:20px;font-weight:700}
.t-company{left:0;width:1200px;top:3428px;text-align:center;color:var(--white);font-size:14px;font-weight:600}

/* footer */
.foot-brand{left:470px;top:3600px;width:260px;display:flex;align-items:center;justify-content:center;gap:8px}
.signup{left:0;width:1200px;top:3690px;text-align:center;color:var(--blue);font-size:19px;font-weight:600}
.news-form{left:373px;top:3730px;width:442px;height:36px;border:1px solid #cfcfcf;display:flex;align-items:center;padding:0 6px 0 12px;gap:10px}
.news-form .field{flex:1;font-size:10px;font-weight:600;color:var(--orange)}
.news-form .submit{background:var(--blue);color:var(--white);font-size:10px;font-weight:600;padding:6px 14px}
.foot-links{left:0;width:1200px;top:3798px;text-align:center;font-size:11px;font-weight:600;color:#222;word-spacing:2px}
.foot-links span{margin:0 12px;color:#555}
.copyright{left:0;width:1200px;top:3838px;text-align:center;font-size:10px;font-weight:600;color:#222}
</style>
</head>
<body>

<!-- HERO -->
<section class="abs hero">
  <div class="abs hero-photo" role="img" aria-label="Photo of a smiling woman sitting on a beach between two golden retrievers" style="background:radial-gradient(ellipse 380px 300px at 600px 460px,rgba(90,150,140,.5),transparent 70%),radial-gradient(ellipse 160px 200px at 400px 480px,rgba(230,200,150,.7),transparent 70%),radial-gradient(ellipse 160px 200px at 820px 480px,rgba(230,200,150,.7),transparent 70%)"></div>
  <div class="abs topbar-email">
    <svg width="18" height="13" viewBox="0 0 18 13"><rect x="0.5" y="0.5" width="17" height="12" fill="none" stroke="#1a6a9a"/><path d="M1 1l8 6 8-6" fill="none" stroke="#1a6a9a"/></svg>
    birchvalecritterden@gmail.com
  </div>
  <div class="abs brand"><span class="brand-dot"></span><span class="brand-name">Birchvale Critter Den</span></div>
  <div class="abs topbar-phone">
    <svg width="16" height="16" viewBox="0 0 24 24"><path d="M6.6 10.8a15 15 0 006.6 6.6l2.2-2.2a1 1 0 011-.25 11.4 11.4 0 003.6.57 1 1 0 011 1V20a1 1 0 01-1 1A17 17 0 013 4a1 1 0 011-1h3.5a1 1 0 011 1c0 1.25.2 2.45.57 3.57a1 1 0 01-.25 1z" fill="none" stroke="#1a6a9a" stroke-width="1.6"/></svg>
    210-555-0148
  </div>
  <nav class="abs nav">
    <a class="active" href="#">PHOTO GALLERY</a>
    <a href="#">ABOUT US</a>
    <a href="#">SERVICES</a>
    <a href="#">POLICIES</a>
    <a href="#">MONTHLY NEWSLETTER</a>
    <a href="#">UNAVAILABLE DATES</a>
    <a href="#">INTRODUCTION</a>
    <a href="#">PAYMENT METHODS</a>
  </nav>
  <div class="abs hero-caption">We provide professional pet sitting</div>
  <div class="abs hero-arrows">
    <svg width="14" height="24" viewBox="0 0 14 24"><path d="M11 3L3 12l8 9" fill="none" stroke="#fff" stroke-width="3"/></svg>
    <svg width="14" height="24" viewBox="0 0 14 24"><path d="M3 3l8 9-8 9" fill="none" stroke="#fff" stroke-width="3"/></svg>
  </div>
</section>

<!-- GALLERY -->
<section class="abs gallery">
  <h2 class="abs sec-title script" style="top:105px;color:var(--white)">Photo Gallery</h2>
  <div class="frame" style="left:195px;top:205px;width:530px;height:340px">
    <div class="ph" role="img" aria-label="Photo of a girl cuddling an orange cat" style="background:linear-gradient(120deg,#6b5a4f,#c99a74 45%,#b57a3c 70%,#5a4a3e)"></div>
    <div class="cap blue">Birchvale Critter Den
      <svg style="position:absolute;right:18px;top:11px" width="36" height="16" viewBox="0 0 36 16"><path d="M8 2L2 8l6 6M28 2l6 6-6 6" fill="none" stroke="#fff" stroke-width="2.5"/></svg>
    </div>
  </div>
  <div class="frame" style="left:738px;top:205px;width:268px;height:162px">
    <div class="ph" role="img" aria-label="Photo of a dog resting indoors" style="background:linear-gradient(135deg,#3d2730,#7a4e5a 55%,#2e1f28)"></div>
    <div class="cap">Birchvale Critter Den</div>
  </div>
  <div class="frame" style="left:738px;top:378px;width:268px;height:167px">
    <div class="ph" role="img" aria-label="Photo of a small white fluffy dog on a wooden floor" style="background:linear-gradient(135deg,#6e4a33,#c9b39c 50%,#5a3b28)"></div>
    <div class="cap">Birchvale Critter Den</div>
  </div>
</section>

<!-- ABOUT -->
<section class="abs about" role="img" aria-label="Faded background photo of a woman with her dogs"></section>
<h2 class="abs sec-title script" style="top:1378px;color:var(--blue)">About Us</h2>
<div class="abs about-rule"></div>
<div class="abs about-portrait" role="img" aria-label="Portrait photo of the owner with her dog"></div>
<div class="abs about-text">
  <p>Hi my name is Maren Holloway and I would love to introduce myself. I am a Licensed Veterinarian Technician from Brookfield, Ohio. My family and I moved to Riverton in 2008. I have dedicated the last 13 years to raising my 2 beautiful children and 5 of my furry babies.</p>
  <p>I have the knowledge and the training to give the special care your pet will need. I was a Licensed Veterinarian Technician Supervisor of a major animal hospital in Brookfield. I have spent 20 years of my life taking care of our friends and would love to do the same for yours.</p>
</div>

<!-- SERVICES BLUE BAND -->
<svg class="abs services-band" width="1200" height="560" viewBox="0 0 1200 560">
  <path d="M0 0H1200V495L620 545 600 560 580 545 0 495Z" fill="#1a6a9a"/>
</svg>
<h2 class="abs sec-title script" style="top:1895px;color:var(--white)">Services</h2>
<div class="abs daily-box"><div role="img" aria-label="Illustration of a dog and cat in a circle with a star"></div></div>
<div class="abs daily-title">DAILY VISIT</div>
<div class="abs daily-price">$25.00<small>(Per visit)</small></div>
<ul class="abs list daily-list" style="left:535px">
  <li>No additional charge for each pet</li>
  <li>Dog walks or play time for your pet</li>
  <li>Feeding and fresh water</li>
  <li>Cleaning up any "accidents", litter boxes, cages</li>
  <li>Pet medication administered if necessary (injections/fluids are extra*)</li>
</ul>
<ul class="abs list daily-list" style="left:790px">
  <li>Meeting individual pet needs</li>
  <li>Turning lights on and off</li>
  <li>Bringing in newspaper and mail</li>
  <li>Watering of indoor/outdoor plants</li>
  <li>Pulling Garbage out</li>
</ul>
<div class="abs btn-details">VIEW DETAILS</div>

<!-- SERVICE CARDS -->
<div class="abs card-icon" style="left:218px;top:2418px"><div role="img" aria-label="Icon of a pet bed"></div></div>
<div class="abs card-title" style="left:360px;top:2408px">POTTY VISITS</div>
<div class="abs card-price" style="left:360px;top:2436px">$10.00</div>
<ul class="abs list card-list" style="left:360px;top:2470px">
  <li>Usually done at noon and bedtime Medication</li>
  <li>letting them out to potty</li>
  <li>some playtime (noon time only)</li>
  <li>checking surroundings</li>
</ul>

<div class="abs card-icon" style="left:613px;top:2418px"><div role="img" aria-label="Icon of a person walking a dog"></div></div>
<div class="abs card-title" style="left:750px;top:2408px">JUST WALKS</div>
<div class="abs card-price" style="left:750px;top:2436px">$15.00/ <small>20 min walk</small></div>
<ul class="abs list card-list" style="left:750px;top:2470px">
  <li>Usually done at noon and bedtime Medication</li>
  <li>letting them out to potty</li>
  <li>some playtime (noon time only)</li>
  <li>checking surroundings</li>
</ul>

<div class="abs card-icon" style="left:218px;top:2638px"><div role="img" aria-label="Icon of a taxi car"></div></div>
<div class="abs card-title" style="left:360px;top:2628px">PET TAXI</div>
<div class="abs card-price" style="left:360px;top:2656px">$10.00</div>
<ul class="abs list card-list" style="left:360px;top:2690px">
  <li>Usually done at noon and bedtime Medication</li>
  <li>letting them out to potty</li>
  <li>some playtime (noon time only)</li>
  <li>checking surroundings</li>
</ul>

<div class="abs card-icon" style="left:613px;top:2638px"><div role="img" aria-label="Icon of a dog"></div></div>
<div class="abs card-title" style="left:750px;top:2628px">DOG PARK</div>
<div class="abs card-price" style="left:750px;top:2656px">$15.00/ <small>20 min walk</small></div>
<ul class="abs list card-list" style="left:750px;top:2690px">
  <li>Usually done at noon and bedtime Medication</li>
  <li>letting them out to potty</li>
  <li>some playtime (noon time only)</li>
  <li>checking surroundings</li>
</ul>

<!-- TESTIMONIALS -->
<svg class="abs" style="left:0;top:2860px" width="1200" height="655" viewBox="0 0 1200 655">
  <path d="M0 45L600 0 1200 45V655H0Z" fill="#1a6a9a"/>
  <path d="M125 325l-10 12 10 12" fill="none" stroke="#d88a0b" stroke-width="4"/>
  <path d="M1073 325l10 12-10 12" fill="none" stroke="#d88a0b" stroke-width="4"/>
</svg>
<h2 class="abs sec-title script" style="top:2970px;color:var(--white)">Testimonials</h2>
<div class="abs quote-mark">&ldquo;</div>
<p class="abs quote-text">Sed ut perspiciatis unde omnis iste natus error sit voluptatem accusantium doloremque laudantium, totam rem aperiam, eaque ipsa quae ab illo inventore veritatis et quasi architecto beatae vitae dicta sunt explicabo. ...</p>
<div class="abs avatar" role="img" aria-label="Portrait photo of the reviewer"></div>
<div class="abs t-name">Owen Calder</div>
<div class="abs t-company">Company Name</div>

<!-- FOOTER -->
<div class="abs foot-brand"><span class="brand-dot"></span><span class="brand-name">Birchvale Critter Den</span></div>
<div class="abs signup">SIGNUP FOR NEWSLETTER</div>
<div class="abs news-form">
  <svg width="14" height="10" viewBox="0 0 14 10"><rect x="0.5" y="0.5" width="13" height="9" fill="none" stroke="#d88a0b"/><path d="M1 1l6 4 6-4" fill="none" stroke="#d88a0b"/></svg>
  <span class="field">ENTER YOUR E-MAIL ADDRESS</span>
  <span class="submit">SUBSCRIBE NOW</span>
</div>
<div class="abs foot-links">PHOTO GALLERY<span>|</span>ABOUT US<span>|</span>SERVICES<span>|</span>POLICIES<span>|</span>MONTHLY NEWSLETTER<span>|</span>UNAVAILABLE DATES<span>|</span>INTRODUCTION<span>|</span>PAYMENT METHODS</div>
<div class="abs copyright">&copy;2016 COMPANY NAME | ALL RIGHTS RESERVED</div>

</body>
</html>
```